Modern Minimalist photo holiday card

I need a few designs for a photo holiday card that is modern , minimalist yet chic. Some examples on the web of things that I like -

http://www.quillnook.com/product/47065/flat_holiday_photo_cards_velvet_comet.html
http://www.quillnook.com/product/48654/flat_holiday_photo_cards_amber_kite.html

http://www.vexorab.com/studio-brisk-minimalist-holiday-card-collection/

Target Market(s)

Customers would be American educated professional living in big cities and suburbs. They will most likely be females from 20 to 50.

Industry/Entity Type

Product

Requirements
Must have
• The cards are 5 by 7 folded. I need the design to support 1 photo preferably taking up the whole space with stylized words. No traditional holiday bells etc. Just a hint of holiday is fine. Need 4 designs to begin with. Please quote for 4 distinct designs as a package. You can use any photo you want.

The users submit their photos so the designs should work with many different photos and should not depend on the content of the photo. Users will be able to change the location of text so text placement can depend on the photo. If the colors are coordinated with the photo please provide some alternate colors ( for user to choose)

```html
<!DOCTYPE html>
<html lang="en">
<head>
<meta charset="utf-8">
<title>Happy Holiday – Its leisure</title>
<link rel="stylesheet" href="https://fonts.googleapis.com/css2?family=Raleway:wght@200;300&display=swap">
<style>
  :root {
    --forest-deep: #0c1a08;
    --forest-shadow: #1c3310;
    --forest-mid: #3f6a1e;
    --leaf-lit: #7fae3c;
    --sun-glow: #fbfff0;
    --type-white: #ffffff;
  }
  html, body {
    margin: 0;
    padding: 0;
    width: 1200px;
    height: 857px;
    overflow: hidden;
    background: var(--forest-deep);
  }
  .card {
    position: relative;
    width: 1200px;
    height: 857px;
    overflow: hidden;
  }
  .card__photo {
    position: absolute;
    inset: 0;
    background:
      radial-gradient(circle at 965px 55px, var(--sun-glow) 0, rgba(251,255,240,0.85) 80px, rgba(200,230,150,0.35) 230px, rgba(127,174,60,0) 420px),
      radial-gradient(ellipse 520px 380px at 620px 320px, rgba(127,174,60,0.45), rgba(127,174,60,0) 100%),
      radial-gradient(ellipse 420px 500px at 1100px 600px, rgba(63,106,30,0.6), rgba(63,106,30,0) 100%),
      linear-gradient(100deg, var(--forest-deep) 0%, var(--forest-shadow) 30%, var(--forest-mid) 60%, var(--forest-shadow) 100%);
  }
  .card__greeting {
    position: absolute;
    left: 48px;
    margin: 0;
    color: var(--type-white);
    font-family: "Raleway", sans-serif;
    font-weight: 300;
    line-height: 1;
    white-space: nowrap;
  }
  .card__greeting--happy {
    top: 489px;
    font-size: 70px;
    letter-spacing: 0.17em;
  }
  .card__greeting--holiday {
    top: 574px;
    font-size: 70px;
    letter-spacing: 0.01em;
  }
  .card__headline {
    position: absolute;
    left: 44px;
    top: 611px;
    margin: 0;
    color: var(--type-white);
    font-family: "Raleway", sans-serif;
    font-weight: 200;
    font-size: 230px;
    line-height: 1;
    letter-spacing: -0.01em;
    white-space: nowrap;
  }
</style>
</head>
<body>
  <main class="card">
    <div class="card__photo" role="img" aria-label="Sunlit forest with moss-draped branches, lush green leaves and pale lilac flowers, sun flaring through the canopy at top right"></div>
    <p class="card__greeting card__greeting--happy">Happy</p>
    <p class="card__greeting card__greeting--holiday">Holiday</p>
    <h1 class="card__headline">Its leisure</h1>
  </main>
</body>
</html>
```